Business Card That Looks Like a Sports Card

Want it to look like a sports trading card. That front should have a baseball player. The back will list our contact info and website info etc.

Contact Information for Business Card

www.ridgecrestathletics.example
visitRCX.example
Email: marcus@ridgecrestathletics.example

Colors

Designer to choose colors to be used in the design.

Requirements
Must have
• Use our current logo and color scheme. Must look like a sports trading card.

```html
<!DOCTYPE html>
<html lang="en">
<head>
<meta charset="utf-8">
<title>Ridgecrest Athletics – Business Card</title>
<link rel="stylesheet" href="https://fonts.googleapis.com/css2?family=Arvo:wght@400;700&family=Nunito:wght@400;600&display=swap">
<style>
  :root {
    --navy: #101c40;
    --teal: #1fae8c;
    --white: #f4f4f2;
    --grey: #c3c5cc;
    --backdrop: #e7e4df;
    --text-light: #e9ecf3;
  }
  * { box-sizing: border-box; margin: 0; padding: 0; }
  html, body { width: 1200px; height: 700px; overflow: hidden; }
  body {
    background: var(--backdrop);
    font-family: "Nunito", sans-serif;
    position: relative;
  }
  .card {
    position: absolute;
    top: 195px;
    width: 540px;
    height: 310px;
    overflow: hidden;
    box-shadow: 0 6px 18px rgba(0,0,0,.18);
  }
  .card-front { left: 40px; background: var(--navy); }
  .card-back { left: 620px; background: var(--navy); }
  .card-art { position: absolute; inset: 0; }

  .brand-mark {
    position: absolute;
    display: flex;
    align-items: center;
    gap: 10px;
    font-family: "Arvo", serif;
    font-weight: 700;
    text-transform: uppercase;
    white-space: nowrap;
  }
  .brand-mark-dot { border-radius: 50%; flex: none; }
  .card-front .brand-mark {
    left: 50%; top: 50%;
    transform: translate(-50%, -50%);
    font-size: 30px;
    color: var(--white);
    letter-spacing: 1px;
  }
  .card-front .brand-mark-dot { width: 26px; height: 26px; background: var(--teal); }
  .card-back .brand-mark {
    left: 412px; top: 138px;
    transform: translateX(-50%);
    font-size: 15px;
    color: var(--navy);
    flex-direction: column;
    gap: 6px;
    text-align: center;
    line-height: 1.15;
  }
  .card-back .brand-mark-dot { width: 20px; height: 20px; background: var(--teal); }

  .contact-block {
    position: absolute;
    left: 34px;
    top: 117px;
    color: var(--text-light);
  }
  .person-name {
    font-family: "Arvo", serif;
    font-size: 17px;
    font-weight: 400;
    color: var(--teal);
    letter-spacing: .5px;
    text-transform: uppercase;
  }
  .person-title {
    font-size: 11.5px;
    letter-spacing: .6px;
    margin-top: 4px;
    text-transform: uppercase;
  }
  .contact-list { list-style: none; margin-top: 17px; }
  .contact-list li {
    display: flex;
    align-items: center;
    gap: 8px;
    font-size: 11.5px;
    line-height: 16px;
  }
  .contact-icon { width: 10px; height: 10px; flex: none; }
</style>
</head>
<body>

<section class="card card-front" aria-label="Business card front">
  <div class="brand-mark">
    <span class="brand-mark-dot"></span>
    <span>Ridgecrest Athletics</span>
  </div>
</section>

<section class="card card-back" aria-label="Business card back">
  <svg class="card-art" viewBox="0 0 540 310" width="540" height="310" aria-hidden="true">
    <rect width="540" height="310" fill="var(--navy)"/>
    <path d="M290 0 C240 50 240 120 290 190 C340 255 400 290 440 310 L540 310 L540 0 Z" fill="var(--teal)"/>
    <path d="M310 0 C262 45 262 115 310 180 C358 245 430 290 470 310 L540 310 L540 0 Z" fill="var(--white)"/>
  </svg>
  <svg class="card-art" viewBox="0 0 540 310" width="540" height="310">
    <g role="img" aria-label="Illustrated basketball peeking over the top edge">
      <circle cx="322" cy="26" r="37" fill="var(--grey)" stroke="var(--navy)" stroke-width="3"/>
    </g>
  </svg>

  <div class="contact-block">
    <h1 class="person-name">Dana Whitfield</h1>
    <p class="person-title">President</p>
    <ul class="contact-list">
      <li>
        <svg class="contact-icon" viewBox="0 0 10 10"><rect x="0.5" y="2" width="9" height="6.5" fill="var(--teal)"/><path d="M0.5 2 L5 5.5 L9.5 2" fill="none" stroke="var(--navy)" stroke-width="1"/></svg>
        marcus@ridgecrestathletics.example
      </li>
      <li>
        <svg class="contact-icon" viewBox="0 0 10 10"><circle cx="5" cy="5" r="4.5" fill="var(--teal)"/><path d="M0.5 5 H9.5 M5 0.5 C2.5 3 2.5 7 5 9.5 M5 0.5 C7.5 3 7.5 7 5 9.5" fill="none" stroke="var(--navy)" stroke-width=".8"/></svg>
        www.visitRCX.example
      </li>
      <li>
        <svg class="contact-icon" viewBox="0 0 10 10"><circle cx="5" cy="5" r="4.5" fill="var(--teal)"/><path d="M0.5 5 H9.5 M5 0.5 C2.5 3 2.5 7 5 9.5 M5 0.5 C7.5 3 7.5 7 5 9.5" fill="none" stroke="var(--navy)" stroke-width=".8"/></svg>
        www.ridgecrestathletics.example
      </li>
    </ul>
  </div>

  <div class="brand-mark">
    <span class="brand-mark-dot"></span>
    <span>Ridgecrest<br>Athletics</span>
  </div>
</section>

</body>
</html>
```